Accounting Business needs double sided DL flyer design

We need a double sided DL flyer designed,
Front side with logo, web address and our short intro.
Backside to have a list of services.
Our colours are blue and a concrete grey colour. Look at our website for a feel for our colour scheme.
www.lanternwellgroup.com.au
I have included the pic from our website to possibly use but we are also open to new creative ideas.
Target Market(s)
Our target market are proactive business owners, particularly in the wine and hospitality industry.
Industry/Entity Type
Business
Look and feel

```html
<!DOCTYPE html>
<html lang="en">
<head>
<meta charset="utf-8">
<title>Lanternwell Group – DL Flyer</title>
<link href="https://fonts.googleapis.com/css2?family=Open+Sans:wght@400;600;700&display=swap" rel="stylesheet">
<style>
  :root {
    --navy: #173a6f;
    --navy-text: #1c3a6b;
    --icon-grey: #3c3c3e;
    --page: #ffffff;
    --concrete-light: #efedeb;
    --concrete-dark: #a9adb4;
    --white: #ffffff;
  }
  * { margin: 0; padding: 0; box-sizing: border-box; }
  html, body { width: 1200px; height: 999px; overflow: hidden; background: var(--page); }
  body { position: relative; font-family: "Open Sans", Arial, sans-serif; color: var(--navy-text); }

  .flyer { position: absolute; left: 303px; width: 595px; height: 281px; overflow: hidden; }
  .flyer--front { top: 205px; }
  .flyer--back { top: 543px; }

  .stair-photo { position: absolute; inset: 0; }
  .flyer--front .stair-photo {
    background: linear-gradient(100deg, var(--concrete-light) 0%, #e6e4e2 45%, #c9cacd 70%, var(--concrete-dark) 100%);
  }
  .flyer--back .stair-photo {
    background: linear-gradient(100deg, #f7f6f5 0%, #f3f2f1 55%, #e4e5e8 80%, #d8dbe1 100%);
  }

  .brand { position: absolute; left: 15px; top: 23px; display: flex; align-items: center; gap: 14px; }
  .brand__mark { width: 40px; height: 40px; background: var(--navy); }
  .brand__name { font-size: 21px; font-weight: 700; color: var(--navy); letter-spacing: 1.5px; text-transform: uppercase; }

  .tagline { position: absolute; left: 45px; top: 106px; font-size: 16px; line-height: 23px; color: var(--navy-text); }

  .contact-box {
    position: absolute; left: 349px; top: 226px; width: 246px; height: 39px;
    background: var(--navy); color: var(--white);
    font-size: 12px; font-weight: 700; line-height: 15px; padding: 4px 0 0 13px;
  }

  .services-heading {
    position: absolute; left: -2px; top: 23px; width: 184px; height: 27px;
    background: var(--navy); color: var(--white);
    font-size: 15px; font-weight: 700; line-height: 27px; padding-left: 60px;
  }

  .service-list { position: absolute; top: 61px; list-style: none; }
  .service-list--left { left: 55px; }
  .service-list--right { left: 352px; }
  .service { display: flex; align-items: center; height: 34px; font-size: 14px; color: var(--navy-text); }
  .service__icon { width: 27px; height: 27px; margin-right: 7px; flex: none; }
</style>
</head>
<body>

<section class="flyer flyer--front">
  <div class="stair-photo" role="img" aria-label="Photo of floating concrete stairs rising along a grey wall with diagonal light"></div>
  <div class="brand">
    <div class="brand__mark"></div>
    <span class="brand__name">Lanternwell Group</span>
  </div>
  <p class="tagline">A guiding hand, a voice of reason,<br>a true partner on the path to success.</p>
  <div class="contact-box">
    www.lanternwellgroup.com.au<br>0400 318 762
  </div>
</section>

<section class="flyer flyer--back">
  <div class="stair-photo" role="img" aria-label="Faded photo of floating concrete stairs on a pale wall"></div>
  <h2 class="services-heading">Our Services</h2>

  <ul class="service-list service-list--left">
    <li class="service"><svg class="service__icon" viewBox="0 0 27 27"><circle cx="13.5" cy="13.5" r="13.5" fill="#3c3c3e"/><rect x="9" y="6.5" width="9" height="14" rx="1" fill="#fff"/><rect x="10.5" y="8" width="6" height="3" fill="#3c3c3e"/></svg>Taxation Compliance</li>
    <li class="service"><svg class="service__icon" viewBox="0 0 27 27"><circle cx="13.5" cy="13.5" r="13.5" fill="#3c3c3e"/><circle cx="13.5" cy="13.5" r="7" fill="#fff"/><path d="M13.5 13.5V6.5A7 7 0 0 1 20.5 13.5Z" fill="#3c3c3e"/></svg>Financial &amp; Management Reporting</li>
    <li class="service"><svg class="service__icon" viewBox="0 0 27 27"><circle cx="13.5" cy="13.5" r="13.5" fill="#3c3c3e"/><path d="M6 12a7.5 6 0 0 1 15 0Z" fill="#fff"/><rect x="13" y="12" width="1.2" height="8" fill="#fff"/></svg>Self-Managed Superannuation</li>
    <li class="service"><svg class="service__icon" viewBox="0 0 27 27"><circle cx="13.5" cy="13.5" r="13.5" fill="#3c3c3e"/><circle cx="13.5" cy="9.5" r="3.5" fill="#fff"/><path d="M7 21a6.5 6 0 0 1 13 0Z" fill="#fff"/></svg>Virtual CFO</li>
    <li class="service"><svg class="service__icon" viewBox="0 0 27 27"><circle cx="13.5" cy="13.5" r="13.5" fill="#3c3c3e"/><rect x="11" y="7" width="5" height="5" fill="#fff"/><rect x="7.5" y="13" width="5" height="5" fill="#fff"/><rect x="14.5" y="13" width="5" height="5" fill="#fff"/></svg>Business Planning</li>
    <li class="service"><svg class="service__icon" viewBox="0 0 27 27"><circle cx="13.5" cy="13.5" r="13.5" fill="#3c3c3e"/><rect x="8" y="15" width="2.5" height="5" fill="#fff"/><rect x="12" y="12" width="2.5" height="8" fill="#fff"/><rect x="16" y="9" width="2.5" height="11" fill="#fff"/></svg>KPIs &amp; Performance Monitoring</li>
  </ul>

  <ul class="service-list service-list--right">
    <li class="service"><svg class="service__icon" viewBox="0 0 27 27"><circle cx="13.5" cy="13.5" r="13.5" fill="#3c3c3e"/><path d="M5 13l5-3h7l5 3-5 4h-7Z" fill="#fff"/></svg>Succession Planning</li>
    <li class="service"><svg class="service__icon" viewBox="0 0 27 27"><circle cx="13.5" cy="13.5" r="13.5" fill="#3c3c3e"/><rect x="8" y="7" width="11" height="13" fill="#fff"/><rect x="10" y="10" width="7" height="1" fill="#3c3c3e"/><rect x="10" y="13" width="7" height="1" fill="#3c3c3e"/></svg>Estate Planning</li>
    <li class="service"><svg class="service__icon" viewBox="0 0 27 27"><circle cx="13.5" cy="13.5" r="13.5" fill="#3c3c3e"/><path d="M8 18a3.5 3.5 0 0 1 1-6.8 4.5 4.5 0 0 1 8.6-0.6A3.8 3.8 0 0 1 19 18Z" fill="#fff"/></svg>Cloud Solutions</li>
    <li class="service"><svg class="service__icon" viewBox="0 0 27 27"><circle cx="13.5" cy="13.5" r="13.5" fill="#3c3c3e"/><circle cx="10" cy="8.5" r="2" fill="#fff"/><rect x="8.5" y="11" width="3" height="9" fill="#fff"/><circle cx="17" cy="8.5" r="2" fill="#fff"/><rect x="15.5" y="11" width="3" height="9" fill="#fff"/></svg>Business Support Services</li>
    <li class="service"><svg class="service__icon" viewBox="0 0 27 27"><circle cx="13.5" cy="13.5" r="13.5" fill="#3c3c3e"/><rect x="15" y="6" width="2" height="4" fill="#fff"/><rect x="14" y="10" width="4" height="10" rx="1" fill="#fff"/><path d="M7.5 9h5a2.5 3 0 0 1-5 0Z" fill="#fff"/><rect x="9.5" y="12" width="1" height="7" fill="#fff"/></svg>The Wine Industry</li>
  </ul>
</section>

</body>
</html>
```